Corporate services company needs a brochure

We are starting a company offering setup services to companies new to that location.
This includes services such as recruitment, company formation, advertising, marketing, pr, handling legal issues, logistics, transportation, procurement,immigration services, corporate gifts, accomodation,entertainment, training, administrative services etc.
Basically taking the setup issues off the hands of the company allowing them focus on their core business.

We are looking to design a professional brochure which would give the potential customers the confidence to entrust us with their needs.

We will be including some copy that can be used but i would very much like for you to bring what i have written to life - adding, deducting and amending where required.

We are looking at a A4 4/6 paged brochure but open to suggestions.

                                       

If you have any images that are suitable, please let us know. We will also be searching for some to add.

The first prize has been increased.

Thanks

Reason: We have just guaranteed the payment and we are hoping that this will encourage good designers to participate.

Reason: Some designers have requested more time to complete their final design.

Hi, I h extended the deadline to give designers more time to work on designs.

we are also looking at making the brochure a height of 8.5 and a width of 11. Please let me know your thoughts on this as any advice will help. The whole objective is to make it look as up to date and creative as possible. There is also another design size of 7.5 by 8.5

Thanks

                                        Hi

The copy has been revised and uploaded.

Hopefully it will give a clearer explanation of what we are trying to do.

Please let me know if you have any further questions.

Thanks

Marta

Reason: adding finishing touches to designs

Reason: We are amending the copy for the brochure

Reason: The new copy for the brochure is ready. I am sorry it has taken so long to get it out. I am sure we will not be making any amendments to it post today. Thanks for your patience The extension is not to attact new designs it is for existing designs's copy to be modified to include information from the updated copy.

Target Market(s)

medium to large companies in banking, telecom, retail etc. It will be viewed by middle and top management.

Industry/Entity Type

Legal

Requirements
Must have
• The brochure must clearly highlight all our services without just listing as this would risk it appearing as if we have just included everything we could think of!,
Please do not do the sitting round the conference table brochure or the typical blue and white brochure.
I desperately need it to be different, unique and serious enough to show that we are capable of handling/managing all what we have included.
Our clients include the many companies starting up an office in Africa.
We are anxious to have the potential clients understand that we will help them setup under any climax/
Nice to have
• modern colours but not too bright. there must still be a clear serious edge to it.
Should not have
• conference room table and people sitting around it.
the typical blue and white brochures often used for these type of services.

```html
<!DOCTYPE html>
<html lang="en">
<head>
<meta charset="utf-8">
<title>What Can We Do? – Services</title>
<link rel="stylesheet" href="https://fonts.googleapis.com/css2?family=Oswald:wght@400;500&family=Open+Sans:ital,wght@0,400;0,700;1,400;1,600&family=Michroma&display=swap">
<style>
  :root {
    --orange: #f28a1e;
    --orange-text: #e9862c;
    --black: #111111;
    --ink: #222222;
    --grey: #444444;
    --paper: #ffffff;
    --rule: #9a9a9a;
    --slope: 0.75;
  }
  * { margin: 0; padding: 0; box-sizing: border-box; }
  html, body { width: 1200px; height: 464px; overflow: hidden; background: var(--paper); }
  .spread { position: relative; width: 1200px; height: 464px; overflow: hidden; background: var(--paper); font-family: "Open Sans", Arial, sans-serif; }

  /* intro corner */
  .intro-bubble { position: absolute; left: -70px; top: -110px; width: 380px; height: 235px; border-radius: 50%; background: var(--paper); border: 1px solid var(--rule); box-shadow: 0 1px 3px rgba(0,0,0,.15); }
  .title-bar { position: absolute; left: 0; top: 20px; width: 236px; height: 26px; background: var(--orange); }
  .title { position: absolute; left: 10px; top: 22px; font-family: "Michroma", sans-serif; font-weight: 400; font-size: 15px; letter-spacing: 3px; color: var(--ink); }
  .intro-head { position: absolute; left: 46px; top: 52px; font-weight: 700; font-size: 8.5px; color: var(--orange); }
  .intro-copy { position: absolute; left: 46px; top: 64px; width: 190px; font-size: 7.3px; line-height: 1.35; color: var(--grey); }
  .teaser { position: absolute; left: 286px; top: 20px; font-style: italic; font-size: 10px; line-height: 1.2; color: var(--ink); }

  /* central band */
  .service-band { position: absolute; left: 0; top: 238px; width: 1200px; height: 42px; background: var(--orange); }
  .band-title { position: absolute; left: 442px; top: 243px; font-family: "Oswald", sans-serif; font-weight: 400; font-size: 24px; letter-spacing: 6px; color: var(--paper); }

  /* diagonal service labels: anchored at lower-left corner, rising to the right */
  .tag { position: absolute; left: var(--x); top: calc(var(--y) - var(--h, 20px)); width: var(--len); height: var(--h, 20px);
         transform-origin: 0 100%; transform: rotate(-53deg);
         display: flex; flex-direction: column; justify-content: center; align-items: center;
         background: var(--black); color: var(--orange); font-family: "Oswald", sans-serif; font-size: 11px; letter-spacing: 2px; line-height: 15px; white-space: nowrap; }
  .tag.two-line { --h: 34px; }

  .joint { position: absolute; width: 18px; height: 18px; }

  /* description copy set in slanted columns beside each label */
  .note { position: absolute; left: var(--x); top: var(--t); width: calc(var(--w) + var(--h) * var(--slope));
          font-size: 7px; line-height: 8px; color: var(--orange-text); text-align: center; }
  .note::before { content: ""; float: left; width: calc(var(--h) * var(--slope)); height: var(--h); shape-outside: polygon(0 0, 100% 0, 0 100%); }
  .note .slant { float: right; width: calc(var(--h) * var(--slope)); height: var(--h); shape-outside: polygon(100% 0, 100% 100%, 0 100%); }
  .note .lead { display: block; font-style: italic; font-weight: 600; color: var(--ink); }
  .note .lead.gap { margin-top: 5px; }
  .note.left { text-align: left; }
  .note.tight { font-size: 6.8px; line-height: 7.6px; }
</style>
</head>
<body>
<main class="spread">
  <div class="intro-bubble"></div>
  <div class="title-bar"></div>
  <h1 class="title">What Can We Do?</h1>
  <h2 class="intro-head">BUSINESS IN CITIES IN NIGERIA</h2>
  <p class="intro-copy">Lagos, Port Harcourt, Abuja etc we offer all types of assistance for business operations/setups. We provide the best packages to setup your business in Abuja or Lagos. And through Telvor or via strategic partners we can offer:</p>
  <p class="teaser">Do you want to test the water before setting up a full fledge office?<br>Want to grow without the costs?</p>

  <div class="service-band"></div>
  <div class="band-title">SERVICES</div>

  <!-- upper labels -->
  <div class="tag" style="--x:45px;--y:246px;--len:132px">Office Setup</div>
  <div class="tag two-line" style="--x:186px;--y:246px;--len:160px"><span>Assisting with the</span><span>Purchase of Property</span></div>
  <div class="tag two-line" style="--x:418px;--y:246px;--len:205px"><span>Business and Residential</span><span>Accommodation</span></div>
  <div class="tag two-line" style="--x:649px;--y:246px;--len:150px"><span>Office Formation and</span><span>Setup Services</span></div>
  <div class="tag" style="--x:850px;--y:246px;--len:218px">Human Recources Services</div>
  <div class="tag two-line" style="--x:1040px;--y:246px;--len:264px"><span>Organizing Work Permits and</span><span>Handling Other Immigration Issues</span></div>

  <!-- lower labels -->
  <div class="tag" style="--x:10px;--y:412px;--len:165px">Relocation Assisting</div>
  <div class="tag two-line" style="--x:125px;--y:446px;--len:195px"><span>Last Minute Catering and</span><span>Corporate Hospitality</span></div>
  <div class="tag" style="--x:308px;--y:362px;--len:98px">Concierge</div>
  <div class="tag" style="--x:608px;--y:418px;--len:170px">Chain Supply Services</div>
  <div class="tag" style="--x:735px;--y:396px;--len:143px">Customer Services</div>
  <div class="tag" style="--x:864px;--y:424px;--len:178px">Complimentary Services</div>
  <div class="tag two-line" style="--x:1072px;--y:448px;--len:198px"><span>Marketing and</span><span>Public Relation Services</span></div>

  <!-- joints on the band -->
  <svg width="0" height="0" style="position:absolute">
    <defs>
      <symbol id="joint" viewBox="0 0 18 18"><path d="M6 0h6v6h6v6h-6v6H6v-6H0V6h6z" fill="#111"/></symbol>
    </defs>
  </svg>
  <svg class="joint" style="left:27px;top:235px"><use href="#joint"/></svg>
  <svg class="joint" style="left:161px;top:235px"><use href="#joint"/></svg>
  <svg class="joint" style="left:393px;top:235px"><use href="#joint"/></svg>
  <svg class="joint" style="left:624px;top:235px"><use href="#joint"/></svg>
  <svg class="joint" style="left:831px;top:235px"><use href="#joint"/></svg>
  <svg class="joint" style="left:1015px;top:235px"><use href="#joint"/></svg>
  <svg class="joint" style="left:92px;top:267px"><use href="#joint"/></svg>
  <svg class="joint" style="left:219px;top:269px"><use href="#joint"/></svg>
  <svg class="joint" style="left:350px;top:268px"><use href="#joint"/></svg>
  <svg class="joint" style="left:693px;top:267px"><use href="#joint"/></svg>
  <svg class="joint" style="left:804px;top:267px"><use href="#joint"/></svg>
  <svg class="joint" style="left:954px;top:267px"><use href="#joint"/></svg>
  <svg class="joint" style="left:1168px;top:269px"><use href="#joint"/></svg>

  <!-- upper descriptions -->
  <p class="note" style="--x:58px;--t:170px;--h:64px;--w:92px"><span class="slant"></span>If you are looking to setup a business in Lagos or rent an office in Lagos, Abuja or any other city in Nigeria, Telvor offers the services you need.</p>
  <p class="note" style="--x:199px;--t:146px;--h:88px;--w:182px"><span class="slant"></span>At Telvor we align ourselves with a number of international real-estate brokers and professional services firms who specialize in introducing international corporate clients in Lagos. Though these alliances, we are able to support firms by offering additional benefits to their already long list of initiatives.<br>We also offer expertise through the full lifecycle from concept feasibility and design services to contract preparation, site management, implementation and commissioning.</p>
  <p class="note" style="--x:431px;--t:156px;--h:78px;--w:120px">Locating and providing office suites in Nigeria. Virtual office package Mail handling, the answering of phone calls in your company name, the use of a local business address in a prestige location.</p>
  <p class="note" style="--x:720px;--t:78px;--h:0px;--w:200px"><span class="lead">COMPANY FORMATION</span>Assisting with business incorporation.<br>Advising on suitable corporate structures.<br>Identifying and vetting appropriate local partners.</p>
  <p class="note tight" style="--x:662px;--t:111px;--h:123px;--w:168px"><span class="slant"></span><span class="lead">START-UP SERVICES</span>General Services<br>Business plan (Review and writing)<br>Web development<br>Logo and brochure design<br>Letterhead and Signage.<br>Obtaining local permits also.<br>Network/IT step and maintenance<br>Phone systems<br>Office building<br>(office partitioning, structured cabling, office furniture etc.)<br>Advertising<br>Cabling<br>Accounts/Bookkeeping/Payroll/Contractors<br>Legal</p>
  <p class="note tight" style="--x:863px;--t:142px;--h:92px;--w:140px"><span class="slant"></span>HR function set-up<br>Employee handbooks and policies<br>Employee Performance Management<br>HR hotline<br>Job description<br>Phone screening<br>Staff screening (referencing and health)<br>Offer letters<br>Training<br>Job posting<br>Recruitment</p>

  <!-- lower descriptions -->
  <p class="note" style="--x:78px;--t:290px;--h:36px;--w:90px"><span class="slant"></span>Including shipping, culture training, sourcing domestic staff.</p>
  <p class="note" style="--x:211px;--t:290px;--h:46px;--w:86px"><span class="slant"></span>Arranging local restaurants or simply ask us to serve gourmet meals directly in your meeting room.</p>
  <p class="note left" style="--x:307px;--t:292px;--h:72px;--w:230px"><span class="lead">WHAT YOUR CONCIERGE CAN HELP WITH:</span>Entertainment, house comforts, personal shopping, relaxation, cars and transportation, personal and business storage, corporate gifts.<span class="lead gap">TRAVEL SERVICES</span>Accomodation, travel, car rental, hospitality and corporate entertainment.</p>
  <p class="note" style="--x:679px;--t:292px;--h:36px;--w:78px"><span class="slant"></span>Warehousing, freight forwarding and logistics services. Procurement services.</p>
  <p class="note" style="--x:803px;--t:292px;--h:18px;--w:62px">Call Centre and CRM Services.</p>
  <p class="note left" style="--x:953px;--t:292px;--h:18px;--w:170px">Introduction sessions on the local culture.<br>Local language classes.</p>
</main>
</body>
</html>
```